Brimvane.com fiber optic internet website redesign

We need a new website design for our fiber optic internet company that provides internet, phone, and tv services. It should use the text "Marrowfen fiber optics", and "I beamed up with Marrowfen". The design should use the color blue and the attached logo.
We are a 30 year old internet company who started as a dial up internet provider in our basement. Today we design, build, and maintain our own fiber optic internet network to provide service to residential, business, educational, healthcare, and governmental customers

```html
<!DOCTYPE html>
<html lang="en">
<head>
<meta charset="utf-8">
<title>Contact Us – Brimvane.com</title>
<link rel="stylesheet" href="https://fonts.googleapis.com/css2?family=Raleway:wght@400;500;600;700&family=Roboto:wght@400;500&display=swap">
<style>
:root{
  --blue:#1b6ac9;
  --blue-dark:#0f56b3;
  --navy:#0a1020;
  --red:#e0201c;
  --ink:#111;
  --muted:#f4f7fc;
  --line:#c9ced8;
  --white:#fff;
}
*{box-sizing:border-box;margin:0;padding:0}
html,body{width:1200px;height:2342px;overflow:hidden}
body{position:relative;font-family:"Raleway",sans-serif;color:var(--ink);background:var(--white)}
.abs{position:absolute}
.hero{position:absolute;left:0;top:0;width:1200px;height:600px;background:radial-gradient(circle at 78% 30%,#3b3a30 0,#1b2233 30%,#0d1526 70%);}
.hero-wave{position:absolute;left:0;top:0}
.topbar-phone{left:796px;top:15px;color:var(--white);font:500 16px "Roboto",sans-serif}
.btn{display:flex;align-items:center;justify-content:center;font:500 14px "Roboto",sans-serif}
.btn-user{left:936px;top:6px;width:91px;height:37px;background:var(--white);color:var(--ink)}
.btn-support{left:1034px;top:6px;width:100px;height:37px;background:var(--blue-dark);color:var(--white)}
.brand{display:flex;align-items:center;gap:10px;color:var(--white);font:600 21px "Raleway",sans-serif}
.brand-dot{width:42px;height:42px;border-radius:50%;background:var(--blue-dark)}
.nav{top:58px;color:var(--white);font:500 15.5px "Roboto",sans-serif}
.nav.active{color:var(--red)}
.hero-title{left:0;width:1200px;top:236px;text-align:center;color:var(--white);font:700 52px "Raleway",sans-serif}
.crumb{left:0;width:1200px;top:318px;text-align:center;color:var(--white);font:400 13px "Roboto",sans-serif}
.crumb span{color:var(--red)}
.h2{font:700 42px "Raleway",sans-serif}
.intro{left:64px;top:673px;font:500 15.5px "Raleway",sans-serif}
.h3{font:500 26px "Raleway",sans-serif}
.hours{left:65px;top:803px;width:270px}
.hours li{list-style:none;display:flex;align-items:center;height:54.4px;font:500 15.5px "Raleway",sans-serif}
.hours .day{white-space:nowrap}
.hours .rule{flex:1;border-top:1px solid var(--line);margin:0 4px}
.hours .time{width:108px}
.icon-box{width:47px;height:46px;background:#eef0f3;border-radius:4px;display:flex;align-items:center;justify-content:center}
.info{font:500 15.5px "Raleway",sans-serif;line-height:26px}
.quick{left:0;top:1185px;width:1200px;height:500px;background:var(--muted)}
.field{background:var(--muted);border:1px solid var(--line);font:400 13px "Roboto",sans-serif;color:#555;padding:0 13px;display:flex;align-items:center}
.submit{left:130px;top:1390px;width:309px;height:51px;background:var(--blue);color:var(--white);font:500 14px "Roboto",sans-serif;display:flex;align-items:center;justify-content:center}
.captcha{left:130px;top:1449px;width:309px;height:76px;background:#f9f9f9;border:1px solid #d3d3d3;border-radius:3px}
.footer-wave{position:absolute;left:0;top:1600px}
.ftext{color:var(--white);font:400 14.5px "Raleway",sans-serif}
.fhead{color:var(--white);font:700 20px "Raleway",sans-serif}
.flinks a{display:block;color:var(--white);text-decoration:none;font:400 14.5px "Roboto",sans-serif;height:32px}
.social{width:38px;height:38px;background:#2a3140}
.circle{width:36px;height:36px;border-radius:50%;background:var(--blue-dark);display:flex;align-items:center;justify-content:center}
.bottom-rule{left:66px;top:2280px;width:1068px;border-top:1px solid #222b3c}
.legal{color:#c5cad6;font:400 10.5px "Roboto",sans-serif;letter-spacing:.5px}
</style>
</head>
<body>

<header>
  <div class="hero" role="img" aria-label="Close-up photo of bundled fiber optic cables with glowing ends"></div>
  <svg class="hero-wave" width="1200" height="600" viewBox="0 0 1200 600">
    <path d="M0 454 C70 370 150 332 230 334 C330 336 400 400 470 452 C590 542 700 588 810 591 C960 594 1110 500 1200 373 L1200 600 L0 600 Z" fill="#fff"/>
    <path d="M0 454 C70 370 150 332 230 334 C330 336 400 400 470 452 C590 542 700 588 810 591 C960 594 1110 500 1200 373" fill="none" stroke="var(--blue)" stroke-width="9"/>
  </svg>
  <div class="abs topbar-phone">1-888-555-0142</div>
  <div class="abs btn btn-user">USER</div>
  <div class="abs btn btn-support">SUPPORT</div>
  <div class="abs brand" style="left:66px;top:47px"><span class="brand-dot"></span>Brimvane.com</div>
  <nav>
    <div class="abs nav" style="left:345px">HOME</div>
    <div class="abs nav" style="left:440px">RESIDENTIAL</div>
    <div class="abs nav" style="left:588px">BUSINESS</div>
    <div class="abs nav" style="left:714px">SERVICES</div>
    <div class="abs nav" style="left:836px">FAQ</div>
    <div class="abs nav" style="left:916px">TELECOM</div>
    <div class="abs nav active" style="left:1037px">CONTACT US</div>
  </nav>
  <h1 class="abs hero-title">Contact us</h1>
  <div class="abs crumb">Home &gt; <span>Contact Us</span></div>
</header>

<main>
  <h2 class="abs h2" style="left:63px;top:606px">Contact Us</h2>
  <p class="abs intro">We would love to hear from you! Please use any of the methods of contact below and we will get back to you as soon as possible. Thanks!</p>

  <h3 class="abs h3" style="left:64px;top:744px">Office Hours</h3>
  <ul class="abs hours">
    <li><span class="day">Sunday</span><span class="rule"></span><span class="time">4pm - 8pm</span></li>
    <li><span class="day">Monday</span><span class="rule"></span><span class="time">8am - 6pm</span></li>
    <li><span class="day">Tuesday</span><span class="rule"></span><span class="time">8am - 6pm</span></li>
    <li><span class="day">Wensday</span><span class="rule"></span><span class="time">8am - 6pm</span></li>
    <li><span class="day">Thursday</span><span class="rule"></span><span class="time">8am - 6pm</span></li>
    <li><span class="day">Friday</span><span class="rule"></span><span class="time">8am - 6pm</span></li>
    <li><span class="day">Saturday</span><span class="rule"></span><span class="time">12pm - 4pm</span></li>
  </ul>

  <div class="abs icon-box" style="left:495px;top:750px">
    <svg width="14" height="18" viewBox="0 0 14 18"><path d="M7 0C3.1 0 0 3 0 6.8 0 11.5 7 18 7 18s7-6.5 7-11.2C14 3 10.9 0 7 0zm0 9.3a2.5 2.5 0 1 1 0-5 2.5 2.5 0 0 1 0 5z" fill="var(--blue)"/></svg>
  </div>
  <h3 class="abs h3" style="left:494px;top:802px">Address</h3>
  <div class="abs info" style="left:493px;top:845px">Marrowfen Inc. 48 Lantern Row<br>Ashdale, PA 16000</div>

  <div class="abs icon-box" style="left:807px;top:750px">
    <svg width="16" height="16" viewBox="0 0 24 24"><path d="M6.6 10.8a15.1 15.1 0 0 0 6.6 6.6l2.2-2.2a1 1 0 0 1 1-.25 11.4 11.4 0 0 0 3.6.57 1 1 0 0 1 1 1V20a1 1 0 0 1-1 1A17 17 0 0 1 3 4a1 1 0 0 1 1-1h3.5a1 1 0 0 1 1 1c0 1.25.2 2.45.57 3.57a1 1 0 0 1-.25 1z" fill="var(--blue)"/></svg>
  </div>
  <h3 class="abs h3" style="left:806px;top:802px">Phone</h3>
  <div class="abs info" style="left:805px;top:845px">724-555-0193<br>Toll Free: 1-888-555-0142</div>

  <div class="abs icon-box" style="left:495px;top:936px">
    <svg width="18" height="14" viewBox="0 0 18 14"><rect x="1" y="1" width="16" height="12" rx="1.5" fill="none" stroke="var(--blue)" stroke-width="1.6"/><path d="M1.5 2l7.5 6 7.5-6" fill="none" stroke="var(--blue)" stroke-width="1.6"/></svg>
  </div>
  <h3 class="abs h3" style="left:494px;top:994px">Email</h3>
  <div class="abs info" style="left:493px;top:1036px">Sales: sales@marrowfen.com<br>Support: support@marrowfen.com</div>

  <section class="abs quick">
    <h2 class="abs h2" style="left:0;width:1200px;text-align:center;top:57px">Quick Contact</h2>
  </section>
  <div class="abs field" style="left:130px;top:1332px;width:309px;height:50px">Name:</div>
  <div class="abs field" style="left:445px;top:1332px;width:310px;height:50px">Email:</div>
  <div class="abs field" style="left:761px;top:1332px;width:309px;height:50px">Phone:</div>
  <div class="abs submit">SUBMIT</div>
  <div class="abs field" style="left:445px;top:1390px;width:625px;height:135px;align-items:flex-start;padding-top:14px">Message:</div>
  <div class="abs captcha">
    <div class="abs" style="left:13px;top:23px;width:28px;height:28px;border:2px solid #c1c1c1;border-radius:2px;background:#fff"></div>
    <div class="abs" style="left:53px;top:29px;font:400 14px 'Roboto',sans-serif">I'm not a robot</div>
    <div class="abs" style="left:234px;top:45px;font:400 9px 'Roboto',sans-serif;color:#555;text-align:center;width:64px">SecureCheck<br><span style="font-size:7.5px">Privacy - Terms</span></div>
  </div>
</main>

<footer>
  <svg class="footer-wave" width="1200" height="742" viewBox="0 0 1200 742">
    <defs>
      <linearGradient id="footBg" x1="0" y1="0" x2="1" y2="1">
        <stop offset="0" stop-color="#08101f"/>
        <stop offset=".6" stop-color="#0c1530"/>
        <stop offset="1" stop-color="#0a1226"/>
      </linearGradient>
    </defs>
    <path d="M0 236 C110 110 260 24 400 23 C520 22 620 80 720 150 C820 220 900 282 982 280 C1080 278 1160 200 1200 145 L1200 742 L0 742 Z" fill="url(#footBg)" role="img" aria-label="Dark background photo of illuminated fiber optic strands"/>
    <path d="M0 236 C110 110 260 24 400 23 C520 22 620 80 720 150 C820 220 900 282 982 280 C1080 278 1160 200 1200 145" fill="none" stroke="var(--blue)" stroke-width="9"/>
  </svg>

  <div class="abs brand" style="left:66px;top:1922px;font-size:30px"><span class="brand-dot" style="width:62px;height:62px"></span>Brimvane.com</div>
  <p class="abs ftext" style="left:66px;top:2012px;width:380px;line-height:22px">Fiber optic-based communications have been used for years by government and industry.</p>
  <div class="abs social" style="left:66px;top:2088px"></div>
  <div class="abs social" style="left:121px;top:2088px"></div>
  <div class="abs social" style="left:175px;top:2088px"></div>

  <div class="abs fhead" style="left:488px;top:1916px">Quick Links</div>
  <div class="abs flinks" style="left:489px;top:1960px">
    <a>Home</a><a>Residential</a><a>Business</a><a>Services</a><a>FAQ</a><a>Telecom</a><a>Contact us</a><a>Users</a><a>Support</a>
  </div>

  <div class="abs fhead" style="left:691px;top:1916px">Contact Us</div>
  <div class="abs circle" style="left:692px;top:1959px"><svg width="11" height="14" viewBox="0 0 14 18"><path d="M7 0C3.1 0 0 3 0 6.8 0 11.5 7 18 7 18s7-6.5 7-11.2C14 3 10.9 0 7 0zm0 9.3a2.5 2.5 0 1 1 0-5 2.5 2.5 0 0 1 0 5z" fill="#fff"/></svg></div>
  <div class="abs ftext" style="left:736px;top:1959px;line-height:21px">48 Lantern Row, Ashdale,<br>PA 16000</div>
  <div class="abs circle" style="left:692px;top:2016px"><svg width="14" height="14" viewBox="0 0 24 24"><path d="M6.6 10.8a15.1 15.1 0 0 0 6.6 6.6l2.2-2.2a1 1 0 0 1 1-.25 11.4 11.4 0 0 0 3.6.57 1 1 0 0 1 1 1V20a1 1 0 0 1-1 1A17 17 0 0 1 3 4a1 1 0 0 1 1-1h3.5a1 1 0 0 1 1 1c0 1.25.2 2.45.57 3.57a1 1 0 0 1-.25 1z" fill="#fff"/></svg></div>
  <div class="abs ftext" style="left:736px;top:2025px">724-555-0193</div>
  <div class="abs circle" style="left:692px;top:2069px"><svg width="15" height="12" viewBox="0 0 18 14"><rect x="1" y="1" width="16" height="12" rx="1.5" fill="none" stroke="#fff" stroke-width="1.8"/><path d="M1.5 2l7.5 6 7.5-6" fill="none" stroke="#fff" stroke-width="1.8"/></svg></div>
  <div class="abs ftext" style="left:736px;top:2078px">sales@marrowfen.com</div>

  <div class="abs fhead" style="left:969px;top:1916px">Support</div>
  <svg class="abs" style="left:969px;top:1962px" width="14" height="14" viewBox="0 0 24 24"><path d="M6.6 10.8a15.1 15.1 0 0 0 6.6 6.6l2.2-2.2a1 1 0 0 1 1-.25 11.4 11.4 0 0 0 3.6.57 1 1 0 0 1 1 1V20a1 1 0 0 1-1 1A17 17 0 0 1 3 4a1 1 0 0 1 1-1h3.5a1 1 0 0 1 1 1c0 1.25.2 2.45.57 3.57a1 1 0 0 1-.25 1z" fill="#fff"/></svg>
  <div class="abs ftext" style="left:991px;top:1960px">1-888-555-0142</div>
  <svg class="abs" style="left:969px;top:2008px" width="17" height="13" viewBox="0 0 18 14"><rect x="1" y="1" width="16" height="12" rx="1.5" fill="none" stroke="#fff" stroke-width="1.6"/><path d="M1.5 2l7.5 6 7.5-6" fill="none" stroke="#fff" stroke-width="1.6"/></svg>
  <div class="abs ftext" style="left:991px;top:2005px">support@marrowfen.com</div>

  <div class="abs bottom-rule"></div>
  <div class="abs legal" style="left:66px;top:2303px">PRIVACY POLICY | TERMS OF CONDITION</div>
  <div class="abs legal" style="left:0;width:1200px;text-align:center;top:2303px;letter-spacing:0">© <span style="color:var(--red)">BRIMVANE</span>, 2024. ALL RIGHTS RESERVED.</div>
</footer>

</body>
</html>
```